Design website landing page

Looking for redesign of www.vorbelt.com website landing page. The existing contents ok but the design need to be changed.
- The product is in EdTech domain, choose the design accordingly.
- Clean and professional look is expected.
- Images can be removed or replaced.
- Should load fast and responsive.
- No changes to the logo is required.
- Don't want to use slow or heavy libraries, best if you can use standard HTML5, CSS3.
- Include Login and Register pages (or options as in the current website).
- Looking for a clean and latest technology product layout for the website.
- Any graphic used should be handed over to us for the implementation.
- Handover should be the full code (HTML, CSS and any images used)

```html
<!DOCTYPE html>
<html lang="en">
<head>
<meta charset="utf-8">
<title>Vorbelt – Edit Smarter and Wiser</title>
<link rel="stylesheet" href="https://fonts.googleapis.com/css2?family=Open+Sans:wght@400;600;700;800&display=swap">
<style>
:root{
  --blue:#1fa3e6;
  --blue-dark:#168fd0;
  --orange:#f57c1f;
  --ink:#1d1d1f;
  --text:#333;
  --muted:#9a9a9a;
  --page:#f3f7fb;
  --white:#fff;
  --slate:#4d4d4d;
  --dark:#3a3a3c;
}
*{box-sizing:border-box;margin:0;padding:0}
html,body{width:1200px;height:3836px;overflow:hidden}
body{font-family:"Open Sans",Arial,sans-serif;background:var(--page);color:var(--text);position:relative}
.abs{position:absolute}
.topline{left:0;top:0;width:1200px;height:18px;background:var(--blue)}
.nav{left:0;top:18px;width:1200px;height:64px;background:var(--white)}
.brand{left:176px;top:33px;display:flex;align-items:center;gap:10px}
.brand-mark{width:26px;height:26px;background:var(--blue);border-radius:4px}
.brand-name{font-weight:800;font-size:21px;letter-spacing:1px;color:var(--slate)}
.nav-link{top:44px;font-size:12px;color:var(--slate)}
.btn{position:absolute;display:flex;align-items:center;justify-content:center;border-radius:22px;font-size:13px;color:var(--white);font-weight:600}
.btn-orange{background:var(--orange)}
.btn-blue{background:var(--blue)}
.btn-white{background:var(--white);color:var(--ink)}
.hero-bg{left:0;top:82px}
.hero-title{left:173px;top:162px;font-size:33px;line-height:37px;font-weight:800;color:var(--white)}
.hero-text{left:175px;top:258px;width:420px;font-size:13px;line-height:20px;color:var(--white)}
.hero-note{left:175px;top:352px;width:400px;font-size:13px;line-height:20px;font-weight:700;color:var(--white)}
.dots{left:177px;top:494px;display:flex;gap:9px}
.dots span{width:5px;height:5px;border-radius:50%;background:rgba(255,255,255,.5)}
.dots span:first-child{background:var(--white)}
.hero-art{left:670px;top:150px;width:365px;height:430px;border-radius:40px 40px 30px 30px;background:linear-gradient(160deg,#2f3a4a 0%,#1e7fc4 45%,#27a05a 85%,#f3b54a 100%);opacity:.9}
.section-title{width:1200px;left:0;text-align:center;font-weight:800;font-size:27px;line-height:37px;color:var(--ink)}
.card{background:var(--white)}
.card-icon{position:absolute;left:30px}
.card-title{position:absolute;left:32px;font-size:16px;line-height:20px;font-weight:700;color:var(--ink)}
.card-text{position:absolute;left:32px;width:150px;font-size:11px;line-height:14px;color:var(--muted)}
.feature-list{position:absolute;left:50px;top:130px;list-style:none}
.feature-list li{font-size:16px;line-height:35px;color:var(--ink);font-weight:600}
.feature-list li::before{content:"•";color:var(--orange);margin-right:14px}
.accent-bar{position:absolute;left:50px;top:0;width:18px;height:100px;background:var(--blue)}
.dark{left:0;top:1488px;width:1200px;height:595px;background:linear-gradient(90deg,#3d3d40 0%,#58585b 35%,#2e2e31 70%,#3a3a3c 100%)}
.dark-title{color:var(--white)}
.dark-sub{left:360px;top:1654px;width:480px;text-align:center;font-size:11px;line-height:14px;color:#aaa}
.skill{top:1724px;width:170px;height:191px;background:var(--white);border-radius:4px}
.skill svg{position:absolute;left:50%;top:38px;transform:translateX(-50%)}
.skill-name{position:absolute;bottom:42px;width:100%;text-align:center;font-size:16px;font-weight:700;color:var(--ink)}
.clients{left:0;top:2083px;width:599px;height:639px;background:var(--blue)}
.partners{left:599px;top:2083px;width:601px;height:639px;background:var(--white)}
.split-title{position:absolute;top:62px;font-size:27px;font-weight:800}
.split-text{position:absolute;top:114px;font-size:11px;line-height:18px}
.badge{position:absolute;width:140px;height:140px;border-radius:50%;background:var(--white)}
.badge::after{content:"";position:absolute;left:26px;top:26px;width:88px;height:88px;border-radius:50%;background:#dfe7ee}
.partners .badge{border:2px solid #edf0f3}
.plan-sub{left:0;width:1200px;top:2846px;text-align:center;font-size:18px;font-weight:700;color:var(--blue)}
.offer{left:304px;top:2902px;width:600px;height:40px;background:var(--slate);color:var(--white);display:flex;align-items:center;justify-content:center;font-size:18px;font-weight:700}
.tabs{top:2985px;height:45px;display:flex;align-items:center;font-size:18px}
.tab-active{left:372px;width:158px;justify-content:center;background:var(--white);border-radius:23px;font-weight:700;color:var(--ink)}
.tab{color:var(--slate)}
.table{left:176px;top:3075px;width:848px;height:494px;background:var(--white);display:flex}
.feat-col{width:268px;height:100%;background:var(--slate);color:var(--white);padding:34px 0 0 38px}
.feat-col h3{font-size:18px;font-weight:700;margin-bottom:16px}
.feat-col li{list-style:none;font-size:13px;line-height:26.8px}
.plan{flex:1;position:relative;border-left:1px solid #eee;text-align:center}
.plan:first-of-type{border-left:0}
.plan-name{position:absolute;top:32px;width:100%;font-size:14px;font-weight:700;color:var(--ink)}
.plan-price{position:absolute;top:95px;width:100%;font-size:27px;font-weight:800;color:var(--blue)}
.plan-old{position:absolute;top:133px;width:100%;font-size:14px;font-weight:700;color:var(--muted);text-decoration:line-through}
.plan-desc{position:absolute;top:265px;left:50%;transform:translateX(-50%);width:120px;font-size:11px;line-height:18px;color:var(--muted)}
.plan .btn{left:50%;transform:translateX(-50%);top:363px;width:128px;height:39px;font-size:14px}
</style>
</head>
<body>
<div class="abs topline"></div>
<header class="abs nav"></header>
<div class="abs brand"><span class="brand-mark"></span><span class="brand-name">VORBELT</span></div>
<span class="abs nav-link" style="left:469px">Features</span>
<span class="abs nav-link" style="left:557px">Articles</span>
<span class="abs nav-link" style="left:636px">Pricing</span>
<span class="abs nav-link" style="left:712px">Contact Us</span>
<a class="btn btn-orange" style="left:813px;top:38px;width:98px;height:28px;font-size:12px">Register</a>
<a class="btn btn-blue" style="left:925px;top:38px;width:98px;height:28px;font-size:12px">Login</a>

<svg class="abs hero-bg" width="1200" height="540" viewBox="0 0 1200 540">
  <path d="M0 0H1200V170C1130 180 1060 240 960 330C860 420 790 430 700 420C600 410 560 440 520 460C440 500 330 460 240 480C140 500 60 540 0 540Z" fill="var(--blue)"/>
</svg>
<h1 class="abs hero-title">EDIT SMARTER AND WISER,<br>MAKE IT A HABIT</h1>
<p class="abs hero-text">An AI-enabled grammar checker to help explore all aspects of your writing, including sentence structure, sentence length, writing style, punctuation, voice, and much more.</p>
<p class="abs hero-note">Vorbelt has been recognized and recommended by NOVA, CTEB.</p>
<a class="btn btn-orange" style="left:177px;top:420px;width:139px;height:37px;font-size:14px">Register Now</a>
<a class="btn btn-white" style="left:334px;top:420px;width:159px;height:37px;font-size:14px">Test Your Skills</a>
<div class="abs dots"><span></span><span></span><span></span><span></span></div>
<div class="abs hero-art" role="img" aria-label="Illustration of a student working at a laptop on a desk"></div>

<h2 class="abs section-title" style="top:676px">YOUR ONE-STOP SOLUTION TO MASTER<br>THE ENGLISH LANGUAGE</h2>

<div class="abs card" style="left:176px;top:794px;width:211px;height:245px">
  <svg class="card-icon" style="top:30px" width="48" height="48" viewBox="0 0 48 48" fill="none" stroke="var(--blue)" stroke-width="3"><rect x="6" y="6" width="36" height="36"/><rect x="2" y="2" width="8" height="8" fill="var(--white)"/><rect x="38" y="2" width="8" height="8" fill="var(--white)"/><rect x="2" y="38" width="8" height="8" fill="var(--white)"/><rect x="38" y="38" width="8" height="8" fill="var(--white)"/><path d="M16 34L24 14L32 34M19 27H29"/></svg>
  <div class="card-title" style="top:96px">ONLINE<br>LANGUAGE LAB</div>
  <div class="card-text" style="top:148px">Access our comprehensive language lab anytime, anywhere, and on any device</div>
</div>
<div class="abs card" style="left:176px;top:1059px;width:211px;height:247px">
  <svg class="card-icon" style="top:30px" width="44" height="44" viewBox="0 0 44 44" fill="var(--blue)"><rect x="2" y="2" width="40" height="26" rx="2"/><rect x="8" y="10" width="28" height="3" fill="var(--white)"/><rect x="8" y="17" width="28" height="3" fill="var(--white)"/><path d="M14 28H30V42L22 36L14 42Z"/></svg>
  <div class="card-title" style="top:89px">CERTIFICATION</div>
  <div class="card-text" style="top:123px">Access our comprehensive language lab anytime, anywhere, and on any device</div>
</div>
<div class="abs card" style="left:412px;top:794px;width:374px;height:512px">
  <div class="accent-bar"></div>
  <ul class="feature-list">
    <li>Practice LSRW Skills</li>
    <li>Real-time Grammar Analysis</li>
    <li>Real-time Speech Analysis</li>
    <li>Personalized Guides</li>
    <li>Vocabulary Builder</li>
    <li>Adaptive Assessments</li>
    <li>Bite-sized Learning</li>
    <li>Certification</li>
  </ul>
</div>
<div class="abs card" style="left:813px;top:794px;width:211px;height:245px">
  <svg class="card-icon" style="top:36px" width="50" height="40" viewBox="0 0 50 40" fill="var(--blue)"><path d="M2 4Q12 0 24 4V38Q12 34 2 38Z"/><path d="M26 4Q38 0 48 4V38Q38 34 26 38Z"/><path d="M31 12H43M31 18H43M31 24H43" stroke="var(--white)" stroke-width="2.5"/></svg>
  <div class="card-title" style="top:96px">MY<br>LIBRARY</div>
  <div class="card-text" style="top:148px">Access our comprehensive language lab anytime, anywhere, and on any device</div>
</div>
<div class="abs card" style="left:813px;top:1059px;width:211px;height:247px">
  <svg class="card-icon" style="top:30px" width="44" height="44" viewBox="0 0 44 44"><rect x="2" y="2" width="26" height="26" rx="3" fill="var(--blue)"/><rect x="16" y="16" width="26" height="26" rx="3" fill="none" stroke="var(--blue)" stroke-width="2.5"/><path d="M21 26H37M29 22V26M24 38Q32 34 35 26M26 30Q30 36 36 38" fill="none" stroke="var(--blue)" stroke-width="2"/></svg>
  <div class="card-title" style="top:89px">NATIVE LANGUAGE<br>SUPPORT</div>
  <div class="card-text" style="top:143px">Access our comprehensive language lab anytime, anywhere, and on any device</div>
</div>
<a class="btn btn-orange" style="left:526px;top:1356px;width:153px;height:40px;font-size:14px">Register Now</a>

<div class="abs dark" role="img" aria-label="Dimmed photo of a student studying at home"></div>
<h2 class="abs section-title dark-title" style="top:1553px">A WORLD OF BETTER<br>COMMUNICATION AWAITS</h2>
<p class="abs dark-sub">Our AI-enabled grammar checker and speech analyzer have everything you need to put you on par with native speakers</p>
<div class="abs skill" style="left:234px">
  <svg width="68" height="66" viewBox="0 0 68 66" fill="none" stroke="var(--slate)" stroke-width="3.5"><path d="M8 40V32A26 26 0 0 1 60 32V40"/><rect x="6" y="38" width="14" height="24" rx="5"/><rect x="48" y="38" width="14" height="24" rx="5"/></svg>
  <div class="skill-name">LISTENING</div>
</div>
<div class="abs skill" style="left:422px">
  <svg width="50" height="70" viewBox="0 0 50 70" fill="none" stroke="var(--slate)" stroke-width="3.5"><rect x="15" y="2" width="20" height="40" rx="10"/><path d="M6 30A19 19 0 0 0 44 30M25 49V66M14 66H36"/></svg>
  <div class="skill-name">SPEAKING</div>
</div>
<div class="abs skill" style="left:610px">
  <svg width="62" height="70" viewBox="0 0 62 70" fill="none" stroke="var(--slate)" stroke-width="3.5"><circle cx="31" cy="14" r="11"/><path d="M4 34L31 42L58 34V62L31 68L4 62Z M31 42V68"/></svg>
  <div class="skill-name">READING</div>
</div>
<div class="abs skill" style="left:800px">
  <svg width="74" height="66" viewBox="0 0 74 66" fill="none" stroke="var(--slate)" stroke-width="3.5"><path d="M60 4L70 14L36 48L24 52L28 40Z"/><path d="M4 60Q20 48 30 60T60 58"/></svg>
  <div class="skill-name">WRITING</div>
</div>
<a class="btn btn-blue" style="left:517px;top:1974px;width:171px;height:38px;font-size:14px">See how it works</a>

<section class="abs clients">
  <h2 class="split-title" style="left:68px;color:var(--white)">OUR CLIENTS</h2>
  <p class="split-text" style="left:70px;width:450px;color:var(--white)">Our client list speaks for itself. We constantly endeavor to give our clients the best possible learning experience, whether they are reputed universities, corporations, colleges, or individuals. With over a million happy customers, we are extremely fortunate to have formed excellent partnerships with some of our esteemed clients.</p>
  <div class="badge" style="left:70px;top:226px"></div>
  <div class="badge" style="left:228px;top:226px"></div>
  <div class="badge" style="left:386px;top:226px"></div>
  <div class="badge" style="left:70px;top:392px"></div>
  <div class="badge" style="left:228px;top:392px"></div>
</section>
<section class="abs partners">
  <h2 class="split-title" style="left:63px;color:var(--ink)">OUR PARTNERS</h2>
  <p class="split-text" style="left:64px;width:460px;color:var(--muted)">We have formed alliances with some of the leading EdTech partners who have worked with us to deliver ever more innovative, effective and successful projects, and their support has been instrumental in achieving our Vision.</p>
  <div class="badge" style="left:68px;top:226px"></div>
  <div class="badge" style="left:226px;top:226px"></div>
  <div class="badge" style="left:384px;top:226px"></div>
  <div class="badge" style="left:68px;top:392px"></div>
  <div class="badge" style="left:226px;top:392px"></div>
</section>

<h2 class="abs section-title" style="top:2803px">FIND THE RIGHT PLAN</h2>
<p class="abs plan-sub">FLEXIBLE PRICING OPTIONS FOR YOUR NEEDS</p>
<div class="abs offer">CTEB/NOVA USERS, CLICK HERE FOR SPECIAL OFFER.</div>
<div class="abs tabs tab-active">PERSONAL</div>
<div class="abs tabs tab" style="left:565px">ACADEMIA</div>
<div class="abs tabs tab" style="left:721px">ENTERPRISE</div>

<div class="abs table">
  <div class="feat-col">
    <h3>FEATURES:</h3>
    <ul>
      <li>Real-time grammar analysis</li>
      <li>Built-in spellchecker</li>
      <li>Style analysis</li>
      <li>Auto-correction</li>
      <li>Local language support</li>
      <li>Self-paced learning</li>
      <li>Real-time speech analysis</li>
      <li>Reading comprehension</li>
      <li>Listening comprehension</li>
      <li>Vocabulary builder</li>
      <li>Grammar assessments</li>
      <li>Adaptive learning content</li>
      <li>Certification</li>
      <li>Chat &amp; email support</li>
    </ul>
  </div>
  <div class="plan">
    <div class="plan-name">3 MONTHS</div>
    <div class="plan-price">₹742</div>
    <div class="plan-old">₹825</div>
    <div class="plan-desc">3 months access to all premium features</div>
    <a class="btn btn-blue">Pick Plan</a>
  </div>
  <div class="plan">
    <div class="plan-name">12 MONTHS*</div>
    <div class="plan-price">₹742</div>
    <div class="plan-old">₹825</div>
    <div class="plan-desc">12 months access to all premium features</div>
    <a class="btn btn-blue">Pick Plan</a>
  </div>
  <div class="plan">
    <div class="plan-name">6 MONTHS</div>
    <div class="plan-price">₹742</div>
    <div class="plan-old">₹825</div>
    <div class="plan-desc">6 months access to all premium features</div>
    <a class="btn btn-blue">Pick Plan</a>
  </div>
</div>
</body>
</html>
```